Body therapist needs a business card

I need a card for my business which is teaching trainings in body therapy, the company is called Wellacombe Educational Group. I teach to massage therapists around Australia, South East Asia and the USA. I am attaching my logo which will guide you as to what colours I would like to have you consider. Please consult my website to find out more about what I do. www.kinetrova.com.au

My name is Gareth Wellacombe. My phone number is (03) 9157 2618 or 0412573086. email is info@kinetrova.com.au

```html
<!DOCTYPE html>
<html lang="en">
<head>
<meta charset="utf-8">
<title>Wellacombe Educational Group — Business Card</title>
<link rel="stylesheet" href="https://fonts.googleapis.com/css2?family=Oswald:wght@500&family=Poppins:wght@400&family=Open+Sans:wght@400&display=swap">
<style>
  :root {
    --stage: #a9a9a9;
    --card: #ffffff;
    --brown: #7a3b12;
    --tan: #9a5a2a;
    --lime: #c4d600;
    --red: #b00d12;
    --ink: #4a4a4a;
    --rule: #6b6b6b;
    --pattern-a: #f1e4de;
    --pattern-b: #f6f3e4;
  }
  * { box-sizing: border-box; margin: 0; padding: 0; }
  html, body { width: 1200px; height: 800px; overflow: hidden; }
  body {
    background: var(--stage);
    display: flex;
    align-items: center;
    justify-content: center;
    gap: 40px;
  }
  .card {
    position: relative;
    width: 525px;
    height: 300px;
    background: var(--card);
    overflow: hidden;
    box-shadow: 0 6px 18px rgba(0,0,0,.25);
  }
  /* front */
  .brand {
    position: absolute;
    left: 34px;
    top: 112px;
    width: 240px;
    display: flex;
    align-items: center;
    gap: 12px;
  }
  .brand-dot {
    flex: none;
    width: 40px; height: 40px;
    border-radius: 50%;
    background: var(--tan);
  }
  .brand-name {
    font-family: "Open Sans", sans-serif;
    font-weight: 400;
    font-size: 20px;
    line-height: 24px;
    color: var(--tan);
  }
  .divider {
    position: absolute;
    left: 296px;
    top: 98px;
    width: 1px;
    height: 82px;
    background: var(--rule);
  }
  .contact {
    position: absolute;
    left: 316px;
    top: 78px;
  }
  .person {
    font-family: "Oswald", sans-serif;
    font-weight: 500;
    font-size: 20px;
    color: var(--brown);
    text-transform: uppercase;
    letter-spacing: .3px;
    margin-bottom: 10px;
  }
  .contact-list { list-style: none; }
  .contact-list li {
    display: flex;
    align-items: center;
    gap: 8px;
    font-family: "Poppins", sans-serif;
    font-size: 12px;
    line-height: 19px;
    color: var(--ink);
  }
  .contact-list svg { width: 10px; height: 10px; fill: var(--brown); flex: none; }
  .bands {
    position: absolute;
    left: 0; right: 0; bottom: 0;
    height: 9px;
    display: flex;
  }
  .band-brown { flex: 0 0 36%; background: var(--tan); }
  .band-lime { flex: 0 0 32%; background: var(--lime); margin-left: 4px; }
  .band-red { flex: 1; background: var(--red); margin-left: 4px; }
  /* back */
  .back-pattern {
    position: absolute;
    inset: 0;
    background: linear-gradient(135deg, var(--pattern-a), var(--pattern-b) 55%, var(--pattern-a));
  }
  .back-mark {
    position: absolute;
    right: 28px;
    bottom: 60px;
    display: flex;
    align-items: center;
    gap: 8px;
  }
  .back-mark .brand-dot { width: 34px; height: 34px; background: var(--brown); }
  .back-mark .brand-name { font-size: 13px; line-height: 16px; color: var(--brown); }
</style>
</head>
<body>
  <section class="card card-front" aria-label="Business card front">
    <div class="brand">
      <span class="brand-dot"></span>
      <span class="brand-name">Wellacombe<br>Educational Group</span>
    </div>
    <div class="divider"></div>
    <div class="contact">
      <p class="person">Gareth Wellacombe</p>
      <ul class="contact-list">
        <li><svg viewBox="0 0 10 10"><path d="M2 0.5l1.8 2.2-1 1.2c.6 1.3 1.6 2.3 2.9 2.9l1.2-1L9.5 8 8 9.5C4 9 1 6 .5 2z"/></svg>(03) 9157 2618</li>
        <li><svg viewBox="0 0 10 10"><rect x="2.5" y="0" width="5" height="10" rx="1"/><rect x="3.3" y="1.2" width="3.4" height="6.4" fill="#fff"/></svg>0412573086</li>
        <li><svg viewBox="0 0 10 10"><rect x="0" y="1.5" width="10" height="7"/><path d="M0 1.5l5 4 5-4" fill="none" stroke="#fff" stroke-width="1"/></svg>info@kinetrova.com.au</li>
        <li><svg viewBox="0 0 10 10"><circle cx="5" cy="5" r="5"/><path d="M0.5 5h9M5 0.5c-2.5 2.5-2.5 6.5 0 9M5 0.5c2.5 2.5 2.5 6.5 0 9" fill="none" stroke="#fff" stroke-width=".8"/></svg>kinetrova.com.au</li>
      </ul>
    </div>
    <div class="bands">
      <span class="band-brown"></span>
      <span class="band-lime"></span>
      <span class="band-red"></span>
    </div>
  </section>

  <section class="card card-back" aria-label="Business card back">
    <div class="back-pattern" role="img" aria-label="Soft repeating pattern of pale brown, lime and pink circles"></div>
    <div class="back-mark">
      <span class="brand-dot"></span>
      <span class="brand-name">Wellacombe</span>
    </div>
  </section>
</body>
</html>
```